Law Firm Business Card

This is a business card for a law firm that serves US military and veterans.

The card must have ONLY the following (we want an uncluttered look):

- Company logo (PNG, GIF, JPEG copies uploaded)
- A tagline reading: "a law firm for service members and veterans"
- My name and title: "Martin Okello" and "Attorney"
- My email: "martin.okello@harborlinecounsel.com"
- My number: "855-FILE-NOW (345-3669)"

We are looking for a clean, simple layout with only the above information, likely printed on a bright white cotton stock. The font of our logo is DIN 1451, and the font used on our website is Helvetica Neue. The color of our logo is #336699, and we probably want the tagline in that color also, and my contact information in a dark grey. Please review our website at www.harborlinecounsel.com to ensure your card design complements our website style.

Thanks and we look forward to seeing your submissions.

A few notes:

- Two-sided submissions are ok
- Please don't add graphics (scales of justice, judges hammer, etc)

```html
<!DOCTYPE html>
<html lang="en">
<head>
<meta charset="utf-8">
<title>Harborline Counsel – Business Card</title>
<link rel="stylesheet" href="https://fonts.googleapis.com/css2?family=Arimo:wght@400;700&family=Barlow+Semi+Condensed:wght@600&display=swap">
<style>
  :root {
    --brand-blue: #336699;
    --band-blue: #3f7aa8;
    --card-white: #f6f6f4;
    --text-white: #ffffff;
    --backdrop: #e9e6df;
  }
  * { box-sizing: border-box; margin: 0; padding: 0; }
  html, body {
    width: 1200px;
    height: 1000px;
    overflow: hidden;
    background: var(--backdrop);
  }
  .stage {
    width: 1200px;
    height: 1000px;
    display: flex;
    align-items: center;
    justify-content: center;
  }
  .card {
    width: 1050px;
    height: 600px;
    background: var(--card-white);
    padding: 16px;
    box-shadow: 0 10px 30px rgba(0,0,0,0.15);
  }
  .card-frame {
    width: 100%;
    height: 100%;
    background: var(--band-blue);
    padding: 26px 26px 40px;
    display: flex;
    flex-direction: column;
  }
  .brand-panel {
    background: var(--card-white);
    height: 206px;
    display: flex;
    flex-direction: column;
    align-items: center;
    justify-content: center;
    gap: 14px;
  }
  .brand-name {
    font-family: "Barlow Semi Condensed", sans-serif;
    font-weight: 600;
    font-size: 76px;
    line-height: 1;
    letter-spacing: 2px;
    text-transform: uppercase;
    color: var(--brand-blue);
  }
  .tagline {
    font-family: "Arimo", sans-serif;
    font-size: 24px;
    color: var(--brand-blue);
  }
  .name-band {
    flex: 1;
    display: flex;
    flex-direction: column;
    align-items: center;
    justify-content: center;
    color: var(--text-white);
    font-family: "Arimo", sans-serif;
  }
  .person-name {
    font-size: 40px;
    line-height: 1.1;
  }
  .person-title {
    font-size: 22px;
    margin-top: 4px;
  }
  .contact-panel {
    background: var(--card-white);
    height: 104px;
    display: flex;
    align-items: center;
    justify-content: center;
    font-family: "Arimo", sans-serif;
    font-size: 24px;
    color: var(--brand-blue);
  }
</style>
</head>
<body>
  <main class="stage">
    <article class="card">
      <div class="card-frame">
        <header class="brand-panel">
          <h1 class="brand-name">Harborline Counsel</h1>
          <p class="tagline">A law firm for service members and veterans</p>
        </header>
        <section class="name-band">
          <p class="person-name">Martin Okello</p>
          <p class="person-title">Attorney</p>
        </section>
        <footer class="contact-panel">
          <p class="contact-line">martin.okello@harborlinecounsel.com &nbsp;-&nbsp; 855-FILE-NOW (345-3669)</p>
        </footer>
      </div>
    </article>
  </main>
</body>
</html>
```